Prosthetic Brochure

Looking for a trifold brochure that highlights our Prosthetic department. Has to have good stock pictures of prosthetic care. Should have Prosthetic Services from our website www.brindlemoorclinic.com I would like it in the same colors of our website.

Target Market(s)

Patients and physicians

Industry/Entity Type

Medical

Requirements
Must have
• Pictures of people helping prosthetic patients and information from the flyer I uploaded and our website under Prosthetic services.
Nice to have
• Same color scheme as our website. Blue with orange highlights
Should not have
• Just prosthetics no pictures of braces ( orthotics)

```html
<!DOCTYPE html>
<html lang="en">
<head>
<meta charset="utf-8">
<title>Meet Our Prosthetic Team – Brindlemoor Limb Clinic Brochure</title>
<link href="https://fonts.googleapis.com/css2?family=Merriweather:wght@700;900&family=Open+Sans:wght@400;600;700;800&display=swap" rel="stylesheet">
<style>
:root{
  --navy:#1b3766;
  --navy-deep:#132a52;
  --orange:#f26a21;
  --ink:#243047;
  --muted:#5b6478;
  --paper:#ffffff;
  --stage:#e9eaec;
  --photo-a:#8ea3bf;
  --photo-b:#c9b59c;
}
*{box-sizing:border-box;margin:0;padding:0}
html,body{width:1200px;height:3824px;overflow:hidden}
body{background:var(--stage);font-family:"Open Sans",Arial,sans-serif;color:var(--ink);position:relative}
.spread{position:absolute;left:40px;width:1120px;height:760px;background:var(--paper);display:flex;box-shadow:0 6px 24px rgba(0,0,0,.15);overflow:hidden}
.spread--outer{top:1092px}
.spread--inner{top:1972px}
.panel{position:relative;width:373.33px;height:100%;overflow:hidden}
.photo{border-radius:4px}

/* back panel */
.back{padding:34px 30px}
.seal{width:110px;height:110px;border-radius:50%;background:var(--navy);border:6px solid var(--paper);box-shadow:0 0 0 3px var(--navy);margin:0 auto 26px}
.back p{font-size:13px;line-height:1.55;margin-bottom:12px}
.back .staff-photo{position:absolute;left:22px;right:22px;top:470px;height:150px;background:linear-gradient(180deg,#eef1f5,var(--photo-a))}
.phone-number{position:absolute;left:30px;bottom:30px;display:flex;align-items:center;gap:10px;font-weight:800;font-size:22px;color:var(--paper);z-index:2}

/* locations */
.locations{background:var(--navy);color:var(--paper);padding:30px 34px}
.locations h2{font-weight:800;font-size:22px;letter-spacing:1px;color:var(--orange);text-align:center;margin-bottom:22px}
.location{display:flex;gap:12px;margin-bottom:18px}
.location .pin{flex:0 0 auto;margin-top:2px}
.location address{font-style:normal;font-size:12.5px;line-height:1.45}
.location .tel{display:inline-block;margin-top:5px;background:var(--orange);color:var(--paper);font-weight:700;font-size:12px;padding:2px 10px;border-radius:3px}

/* cover */
.cover{background:var(--navy);color:var(--paper);text-align:center}
.cover .brand{padding-top:34px}
.brand-mark{display:inline-flex;align-items:center;gap:8px;font-weight:800;font-size:26px;color:var(--navy);background:var(--paper);padding:6px 14px;border-radius:4px}
.brand-mark .dot{width:16px;height:16px;border-radius:50%;background:var(--orange)}
.brand-sub{font-size:11px;font-weight:600;margin-top:6px}
.tagline{font-size:14px;font-weight:600;margin-top:16px;line-height:1.35}
.tagline em{font-style:normal;color:var(--orange);font-weight:800}
.cover .team-photo{margin:18px 26px 0;height:250px;background:linear-gradient(180deg,#d8dee8,var(--photo-a) 60%,#5d7397)}
.cover h1{font-family:"Merriweather",serif;font-weight:900;font-size:40px;line-height:1.08;margin-top:26px}
.cover h1 span{color:var(--orange)}
.web{position:absolute;left:50%;bottom:58px;transform:translateX(-50%);background:var(--orange);color:var(--paper);font-size:13px;font-weight:700;padding:4px 14px;border-radius:3px;white-space:nowrap;z-index:2}
.swoosh{position:absolute;left:0;bottom:0;width:100%;height:120px}

/* inner */
.why{padding:32px 30px}
.why h3{font-size:16px;font-weight:800;color:var(--navy);margin-bottom:14px}
.why ul{list-style:none}
.why li{position:relative;padding-left:18px;font-size:12.5px;line-height:1.5;margin-bottom:10px}
.why li::before{content:"";position:absolute;left:0;top:6px;width:8px;height:8px;border-radius:50%;background:var(--orange)}
.why li b{color:var(--navy)}
.why .closing{color:var(--orange);font-weight:700;font-size:13px;margin-top:6px}
.consult{margin-top:20px;display:flex;align-items:center;gap:12px;border:2px solid var(--navy);border-radius:30px;padding:10px 16px}
.consult p{font-size:13px;line-height:1.35}
.consult b{color:var(--navy);font-size:15px}
.why .call{position:absolute;left:30px;bottom:26px;font-weight:800;font-size:22px;color:var(--paper);z-index:2}
.team .web{bottom:26px}

.team{padding:28px 22px}
.bio{display:flex;gap:14px;margin-bottom:22px}
.bio .photo{flex:0 0 92px;height:104px;background:linear-gradient(160deg,var(--photo-b),var(--photo-a))}
.bio h4{font-size:12px;font-weight:800;color:var(--navy);line-height:1.3}
.bio .cred{font-size:11px;font-weight:700;color:var(--orange);line-height:1.3;margin-bottom:4px}
.bio p{font-size:11px;line-height:1.45;color:var(--muted)}
.child-photo{position:absolute;right:20px;bottom:30px;width:170px;height:150px;background:linear-gradient(160deg,#f3d8b9,#e98a4c);z-index:2}
</style>
</head>
<body>

<section class="spread spread--outer" aria-label="Brochure outside">
  <div class="panel back">
    <div class="seal" role="img" aria-label="Accreditation seal"></div>
    <p>Brindlemoor Limb Clinic has been providing quality, compassionate care to residents of Riverton and the southern valley since 1983.</p>
    <p>A recognized leader in the field, our experts work as a team to create the most functional solution to your prosthetic needs using the latest technology available.</p>
    <p>Our patient-centered, team approach means we work closely with your doctors, care team and family to deliver a great-fitting prosthetic device that works for you.</p>
    <div class="photo staff-photo" role="img" aria-label="Clinic staff standing together in white coats and scrubs"></div>
    <svg class="swoosh" viewBox="0 0 373 120" preserveAspectRatio="none" aria-hidden="true">
      <path d="M0 40 Q190 10 373 50 V120 H0Z" fill="var(--orange)"/>
      <path d="M0 52 Q190 24 373 62 V120 H0Z" fill="var(--navy)"/>
    </svg>
    <div class="phone-number">
      <svg width="22" height="22" viewBox="0 0 24 24" aria-hidden="true"><path fill="#fff" d="M6.6 10.8a15 15 0 006.6 6.6l2.2-2.2c.3-.3.7-.4 1-.2 1.1.4 2.3.6 3.6.6.6 0 1 .4 1 1V20c0 .6-.4 1-1 1A17 17 0 013 4c0-.6.4-1 1-1h3.5c.6 0 1 .4 1 1 0 1.3.2 2.5.6 3.6.1.3 0 .7-.2 1z"/></svg>
      Call: (555) 014-2280
    </div>
  </div>

  <div class="panel locations">
    <h2>LOCATIONS</h2>
    <div class="location">
      <svg class="pin" width="18" height="24" viewBox="0 0 18 24" aria-hidden="true"><path fill="var(--orange)" d="M9 0a9 9 0 00-9 9c0 7 9 15 9 15s9-8 9-15a9 9 0 00-9-9zm0 12a3 3 0 110-6 3 3 0 010 6z"/></svg>
      <address>22 Linden Court<br>Ashford Hills, KS 66901<br><span class="tel">(555) 014-2280</span></address>
    </div>
    <div class="location">
      <svg class="pin" width="18" height="24" viewBox="0 0 18 24" aria-hidden="true"><path fill="var(--orange)" d="M9 0a9 9 0 00-9 9c0 7 9 15 9 15s9-8 9-15a9 9 0 00-9-9zm0 12a3 3 0 110-6 3 3 0 010 6z"/></svg>
      <address>Brindlemoor North Office<br>880 Quarry Lane, Unit 3<br>Riverton, KS 66950<br><span class="tel">(555) 014-3391</span></address>
    </div>
    <div class="location">
      <svg class="pin" width="18" height="24" viewBox="0 0 18 24" aria-hidden="true"><path fill="var(--orange)" d="M9 0a9 9 0 00-9 9c0 7 9 15 9 15s9-8 9-15a9 9 0 00-9-9zm0 12a3 3 0 110-6 3 3 0 010 6z"/></svg>
      <address>62 Tamsin Road<br>Riverton, KS 66952<br><span class="tel">(555) 014-4472</span></address>
    </div>
    <div class="location">
      <svg class="pin" width="18" height="24" viewBox="0 0 18 24" aria-hidden="true"><path fill="var(--orange)" d="M9 0a9 9 0 00-9 9c0 7 9 15 9 15s9-8 9-15a9 9 0 00-9-9zm0 12a3 3 0 110-6 3 3 0 010 6z"/></svg>
      <address>3105 Coleridge Way<br>Dunmore, KS 66978<br><span class="tel">(555) 014-5503</span></address>
    </div>
    <div class="location">
      <svg class="pin" width="18" height="24" viewBox="0 0 18 24" aria-hidden="true"><path fill="var(--orange)" d="M9 0a9 9 0 00-9 9c0 7 9 15 9 15s9-8 9-15a9 9 0 00-9-9zm0 12a3 3 0 110-6 3 3 0 010 6z"/></svg>
      <address>19 Fennick Street<br>Eastbrook, KS 66983<br><span class="tel">(555) 014-6614</span></address>
    </div>
  </div>

  <div class="panel cover">
    <div class="brand">
      <span class="brand-mark"><span class="dot"></span>Brindlemoor</span>
      <div class="brand-sub">Brindlemoor Limb Clinic</div>
    </div>
    <div class="tagline">We Are Making <em>A Difference</em><br>In People's Life</div>
    <div class="photo team-photo" role="img" aria-label="Prosthetic team group photo"></div>
    <h1>Meet Our<br><span>Prosthetic</span><br>Team</h1>
    <svg class="swoosh" viewBox="0 0 373 120" preserveAspectRatio="none" aria-hidden="true">
      <path d="M0 60 Q200 20 373 70 V120 H0Z" fill="var(--orange)"/>
      <path d="M0 76 Q200 38 373 86 V120 H0Z" fill="var(--paper)"/>
      <path d="M0 90 Q200 56 373 100 V120 H0Z" fill="var(--navy-deep)"/>
    </svg>
    <div class="web">www.brindlemoorclinic.com</div>
  </div>
</section>

<section class="spread spread--inner" aria-label="Brochure inside">
  <div class="panel why">
    <h3>Why use Brindlemoor Limb Clinic?</h3>
    <ul>
      <li><b>First-class patient care</b> – Our facility is accredited by the national board for prosthetic care and we hold the highest standards for patient comfort and safety.</li>
      <li><b>High-end technology</b> – We fit and design devices with the latest and most effective materials available.</li>
      <li><b>Local Fabrication Facility</b> – Our fabrication lab is on site, so repairs and fittings happen fast.</li>
      <li><b>Experience</b> – Decades of combined technical and clinical experience.</li>
      <li><b>Fast turnaround</b> – Same-week fitting for most patients.</li>
      <li><b>A firm belief in teamwork</b> – We work with the patient, rehabilitation staff and physicians to achieve the best outcome.</li>
    </ul>
    <p class="closing">All of these combined allow us to provide the best possible outcome.</p>
    <div class="consult">
      <svg width="34" height="34" viewBox="0 0 24 24" aria-hidden="true"><circle cx="12" cy="12" r="12" fill="var(--navy)"/><path fill="#fff" d="M8.2 10.9a9 9 0 004 4l1.3-1.3c.2-.2.4-.2.6-.1.7.2 1.4.4 2.2.4.3 0 .6.3.6.6v2c0 .3-.3.6-.6.6A10 10 0 016 7.1c0-.3.3-.6.6-.6h2c.3 0 .6.3.6.6 0 .8.1 1.5.4 2.2 0 .2 0 .4-.2.6z"/></svg>
      <p>Call us today for a<br><b>Free consult</b> and<br><b>Prosthetic Check-up</b></p>
    </div>
    <svg class="swoosh" viewBox="0 0 373 120" preserveAspectRatio="none" aria-hidden="true">
      <path d="M0 40 Q190 70 373 30 V120 H0Z" fill="var(--orange)"/>
      <path d="M0 54 Q190 84 373 44 V120 H0Z" fill="var(--navy)"/>
    </svg>
    <div class="call">Call: (555) 014-2280</div>
  </div>

  <div class="panel team">
    <div class="bio">
      <div class="photo" role="img" aria-label="Portrait of Daniel Harwick"></div>
      <div>
        <h4>DANIEL HARWICK, CPO</h4>
        <div class="cred">Board Certified Prosthetist &amp; Orthotist</div>
        <p>Daniel has practiced since 1998 and leads the clinic's upper and lower limb program with a focus on active adults.</p>
      </div>
    </div>
    <div class="bio">
      <div class="photo" role="img" aria-label="Portrait of Owen Marlowe"></div>
      <div>
        <h4>OWEN MARLOWE, CPO</h4>
        <div class="cred">Board Certified Prosthetist</div>
        <p>Owen joined the team after residency and specializes in microprocessor knees and sports limbs.</p>
      </div>
    </div>
    <div class="bio">
      <div class="photo" role="img" aria-label="Portrait of Nora Bellamy"></div>
      <div>
        <h4>NORA BELLAMY, CPO</h4>
        <div class="cred">Board Certified Prosthetist &amp; Orthotist</div>
        <p>Nora focuses on first-time amputees and guides each patient through fitting, training and follow-up.</p>
      </div>
    </div>
    <svg class="swoosh" viewBox="0 0 373 120" preserveAspectRatio="none" aria-hidden="true">
      <path d="M0 30 Q190 60 373 50 V120 H0Z" fill="var(--orange)"/>
      <path d="M0 44 Q190 74 373 64 V120 H0Z" fill="var(--navy)"/>
    </svg>
    <div class="web">www.brindlemoorclinic.com</div>
  </div>

  <div class="panel team">
    <div class="bio">
      <div class="photo" role="img" aria-label="Portrait of Clara Whitfield"></div>
      <div>
        <h4>CLARA WHITFIELD, CPO</h4>
        <div class="cred">Board Certified Prosthetist</div>
        <p>Clara works closely with rehab staff to design comfortable sockets for daily living.</p>
      </div>
    </div>
    <div class="bio">
      <div class="photo" role="img" aria-label="Portrait of Simon Ashgrove"></div>
      <div>
        <h4>SIMON ASHGROVE, CPO</h4>
        <div class="cred">Board Certified Prosthetist &amp; Orthotist</div>
        <p>Simon brings ten years of lab experience and handles complex partial foot and hand cases.</p>
      </div>
    </div>
    <div class="bio">
      <div class="photo" role="img" aria-label="Portrait of Ruth Calloway-Penn"></div>
      <div>
        <h4>RUTH CALLOWAY-PENN, CPO</h4>
        <div class="cred">Board Certified Prosthetist</div>
        <p>Ruth cares for pediatric patients and families.</p>
      </div>
    </div>
    <div class="photo child-photo" role="img" aria-label="Young child with a prosthetic leg playing outdoors"></div>
    <svg class="swoosh" viewBox="0 0 373 120" preserveAspectRatio="none" aria-hidden="true">
      <path d="M0 50 Q190 80 373 40 V120 H0Z" fill="var(--orange)"/>
      <path d="M0 64 Q190 94 373 54 V120 H0Z" fill="var(--navy)"/>
    </svg>
  </div>
</section>

</body>
</html>
```